Educational Agency in Abu Dhabi looking for an 8 pages website

We are looking for an 8 pages design for a website, we already have one but we need to refine it and it is www.korvalendi.ae - Please base it on logo colours (attached) I have uploaded our logo, website content logo colors to use it for the scheme.
We are looking for a smooth look and content added if possible, I also attached content and logo

Industry/Entity Type

Education

Coding

Coded - Design and coding required

Number of Pages Required

5+ page

```html
<!DOCTYPE html>
<html lang="en">
<head>
<meta charset="utf-8">
<title>Korvalendi – Menu</title>
<link href="https://fonts.googleapis.com/css2?family=Roboto:wght@300;400;500;700&display=swap" rel="stylesheet">
<style>
  :root {
    --navy: #1e3264;
    --pink: #ff3566;
    --grey-btn: #c4c5c7;
    --text: #5d5d5d;
    --heading: #2e2e2e;
    --muted: #b9b9b9;
    --rule: #cfcfcf;
    --white: #ffffff;
  }
  * { box-sizing: border-box; margin: 0; padding: 0; }
  html, body { width: 1200px; height: 1200px; overflow: hidden; background: var(--white); font-family: "Roboto", sans-serif; }
  .stage { position: relative; width: 1200px; height: 1200px; }
  .backdrop { position: absolute; left: 0; top: 0; width: 1200px; height: 804px; background: var(--navy); }
  .menu-panel { position: absolute; left: 48px; top: 48px; width: 1104px; height: 708px; background: var(--white); }
  .top-actions { position: absolute; top: 0; left: 936px; display: flex; }
  .apply-btn {
    width: 84px; height: 84px; background: var(--pink); color: var(--white);
    display: flex; align-items: center; justify-content: center; text-align: center;
    font-size: 14px; line-height: 14px; font-weight: 400; text-decoration: none;
  }
  .close-btn { width: 84px; height: 84px; background: var(--grey-btn); display: flex; align-items: center; justify-content: center; }
  .brand { position: absolute; left: 184px; top: 118px; display: flex; align-items: center; gap: 10px; }
  .brand-mark { width: 22px; height: 22px; background: var(--navy); }
  .brand-name { font-size: 22px; font-weight: 700; color: var(--navy); letter-spacing: 1px; }
  .nav-col { position: absolute; top: 212px; list-style: none; }
  .nav-col.main { left: 192px; }
  .nav-col.destinations { left: 566px; }
  .nav-col li { height: 38.4px; font-size: 19px; font-weight: 400; color: var(--text); line-height: 28px; }
  .nav-col li.active { color: var(--pink); }
  .nav-col li.col-heading { color: var(--heading); font-weight: 500; }
  .divider { position: absolute; left: 96px; top: 665px; width: 1016px; height: 1px; background: var(--rule); }
  .contact-line { position: absolute; left: 95px; top: 699px; font-size: 17px; font-weight: 400; color: var(--muted); white-space: pre; }
  .social { position: absolute; left: 872px; top: 690px; display: flex; gap: 7.6px; }
  .social span { width: 42px; height: 42px; border-radius: 4px; background: var(--grey-btn); }
</style>
</head>
<body>
<div class="stage">
  <div class="backdrop"></div>
  <div class="menu-panel"></div>

  <div class="top-actions">
    <a class="apply-btn" href="#">APPLY<br>NOW</a>
    <div class="close-btn" aria-label="Close menu">
      <svg width="26" height="26" viewBox="0 0 26 26"><path d="M1 1L25 25M25 1L1 25" stroke="#ffffff" stroke-width="1.6"/></svg>
    </div>
  </div>

  <div class="brand">
    <span class="brand-mark"></span>
    <span class="brand-name">KORVALENDI</span>
  </div>

  <ul class="nav-col main">
    <li class="active">Home</li>
    <li>About Us</li>
    <li>Services</li>
    <li>Why Study Abroad</li>
    <li>English &amp; Other Languages</li>
    <li>Study Online</li>
    <li>Apply Now</li>
    <li>Contact Us</li>
  </ul>

  <ul class="nav-col destinations">
    <li class="col-heading">STUDY DESTINATIONS</li>
    <li>Study in UK</li>
    <li>Study in USA</li>
    <li>Study in Australia</li>
    <li>Study in New Zealand</li>
    <li>Study in Europe</li>
    <li>Study in Malaysia</li>
    <li>Study in China</li>
    <li>Study in Germany</li>
  </ul>

  <div class="divider"></div>
  <p class="contact-line">Phone: +971 2 555 01 84    |     Email: info@korvalendi.ae</p>

  <div class="social">
    <span aria-label="Social link"></span>
    <span aria-label="Social link"></span>
    <span aria-label="Social link"></span>
    <span aria-label="Social link"></span>
    <span aria-label="Social link"></span>
  </div>
</div>
</body>
</html>
```